Speciality Coffee Shop
Project: Speciality Coffee Shop
Speciality Coffee Shop - Beverages
Creative Brief
Beverages
We chose the name Vireo because it defines the base of coffee and its beginning however our cafe will be serving unique and innovative new drinks which will allow people with different tastes to enjoy the drink. Please update the attached company profile based on the points discussed in the details.
Tornqel58 Tornqel58
Draft #2 : I understand however can you please add a few more slides an input the extra information i provided in the last comment?
Pelomir Pelomir
Hello thanks for rating and comment. First thing we are not professional content writer we are designer. Text content should be provided. You need to hire professional writer for this purpose. I hope you got my point. What I can do is to add the image as you said. Because that is related to design.
Draft #2 : Great job! You are going in the right direction but please find the comments below: 1. The first image you used looks nice but please add other images related to specialty coffee in other slides (such as a Q45 or Slow Brew) 2. Please do not Copy and Paste the text that i gave but use it as a reference. Feel free to change the text to make it more professional. 3. We need a more information on our company profile. Please find below a list of Q&A's for your refference. You can use some of my answers and put them in the profile. Q&A Q: Where is the coffee from? the origin or country imported from A: Colombia, Ethiopia, Kenya, and Panama Q: What is Specialty Coffee? A: According to the Premium Bean Guild of Norland (PBGN), coffee which scores 80 points or above on a 100-point scale is graded "specialty." Specialty coffees are grown in special and ideal climates, and are distinctive because of their full cup taste and little to no defects. In general, we will only select our coffee from suppliers that are certified to be specialty coffee suppliers. Q: Taste A: Each coffee bean tastes different. Some have an after taste of nuts and other have a flowery taste and many more tastes. Weather our customers like their coffee strong (such as an espresso) or sweet (such as our unique Lattes) we will cater to all needs. Q: Short brief on each investor. A: We do not require a brief on each investor individually. The 4 investors Tarek Bensouda, Yousef Qandil, Omar Zaytouni and Hamza Raddaoui have been friends since college. We always had a passion for coffee and were continuously looking for great coffee shops around the country as well as abroad. We finally decided to open our own specialty coffee to ensure that people can trust that it is a specialty coffee shop built by passion rather than financial goals. Q: What are your value propositions or unique selling propositions? A: We will only serve the world's finest specialty coffee, independently tested and scored by certified graders. All our baristas will be certified in the entire aspects of coffee. They will have knowledge from bean to cup to unique latte art. Quality is our number 1 goal. We will never reduce the quality of our items no matter what. Q: What are your vision & mission Our vision is to be the world benchmark for quality coffee. (Please try to think of something better) Our mission is to gather people together over a cup of coffee. (Please try to think of something better.

```html
<!DOCTYPE html>
<html lang="en">
<head>
<meta charset="utf-8">
<title>Vireo – Company Profile</title>
<link rel="stylesheet" href="https://fonts.googleapis.com/css2?family=Montserrat:wght@400;600;700&family=Great+Vibes&family=Playfair+Display:ital,wght@1,400;1,600&family=Open+Sans:wght@400;600&display=swap">
<style>
  :root {
    --stage: #7f7f7f;
    --page: #111111;
    --page-soft: #1b1b1b;
    --ink: #ffffff;
    --ink-muted: #c9c9c9;
    --line: #e6e6e6;
    --box: rgba(0, 0, 0, 0.72);
    --coffee-dark: #2a1a10;
    --coffee-mid: #6b4526;
    --coffee-light: #c9a07a;
  }
  * { box-sizing: border-box; margin: 0; padding: 0; }
  html, body { width: 1200px; height: 967px; overflow: hidden; }
  body { background: var(--stage); position: relative; font-family: "Open Sans", sans-serif; color: var(--ink); }

  .page { position: absolute; width: 570px; height: 430px; background: var(--page); overflow: hidden; box-shadow: 0 6px 18px rgba(0,0,0,0.35); }
  .page--about { left: 20px; top: 30px; }
  .page--concept { left: 610px; top: 30px; }
  .page--vision { left: 20px; top: 505px; }
  .page--specialty { left: 610px; top: 505px; }

  .photo { position: absolute; }
  .brand { position: absolute; display: flex; align-items: center; gap: 8px; font-family: "Montserrat", sans-serif; font-weight: 700; font-size: 30px; letter-spacing: 6px; color: var(--ink); text-transform: uppercase; }
  .brand__dot { width: 9px; height: 9px; border-radius: 50%; background: var(--ink); }

  .heading { font-family: "Montserrat", sans-serif; font-weight: 600; font-size: 15px; color: var(--ink); margin-bottom: 5px; }
  .body-text { font-size: 9.5px; line-height: 1.5; color: var(--ink-muted); }

  /* page 1 */
  .page--about .photo { left: 0; top: 0; width: 390px; height: 430px; background: radial-gradient(circle at 48% 50%, var(--coffee-light) 0%, var(--coffee-mid) 22%, var(--coffee-dark) 45%, #0b0706 75%); }
  .page--about .brand { left: 24px; top: 22px; }
  .info-box { position: absolute; background: var(--box); padding: 10px 12px; }
  .info-box--about { left: 14px; bottom: 14px; width: 175px; height: 92px; }
  .info-box--market { left: 198px; bottom: 14px; width: 178px; height: 92px; }
  .menu { position: absolute; right: 0; top: 0; width: 180px; height: 430px; background: var(--page-soft); border-left: 1px solid #333; padding: 22px 18px; text-align: center; }
  .menu__title { font-family: "Great Vibes", cursive; font-size: 30px; margin-bottom: 12px; }
  .menu__group { font-family: "Great Vibes", cursive; font-size: 22px; margin: 8px 0 4px; }
  .menu__list { list-style: none; font-size: 10.5px; line-height: 1.75; color: var(--ink-muted); }
  .menu__rule { width: 60px; height: 1px; background: var(--line); margin: 8px auto; opacity: .5; }

  /* page 2 */
  .page--concept .photo { right: 0; top: 0; width: 270px; height: 430px; background: linear-gradient(160deg, #3a2a1e 0%, #8d6a4e 40%, #d8c1a6 58%, #5a3c26 78%, #1a110b 100%); }
  .page--concept .brand { left: 22px; top: 20px; font-size: 24px; }
  .concept-block { position: absolute; left: 22px; width: 270px; }
  .concept-block--design { top: 78px; }
  .concept-block--investors { top: 170px; }
  .investor-row { position: absolute; left: 22px; bottom: 22px; display: flex; gap: 12px; }
  .investor-card { width: 82px; height: 72px; border: 1px solid var(--line); border-radius: 4px; display: flex; align-items: flex-end; justify-content: center; padding: 6px; font-size: 8.5px; text-align: center; color: var(--ink-muted); }

  /* page 3 */
  .page--vision .photo { right: 0; top: 0; width: 320px; height: 430px; background: radial-gradient(ellipse at 55% 60%, #7a5638 0%, #3b2718 35%, #120c08 75%); }
  .statement { position: absolute; left: 36px; width: 200px; border: 1.5px solid var(--line); border-radius: 8px; background: #000; padding: 10px 14px; text-align: center; }
  .statement--vision { top: 28px; }
  .statement--mission { top: 300px; }
  .statement__title { font-family: "Playfair Display", serif; font-style: italic; font-weight: 600; font-size: 20px; margin-bottom: 4px; }
  .statement__text { font-family: "Playfair Display", serif; font-style: italic; font-size: 11.5px; line-height: 1.4; }
  .page--vision .brand { left: 58px; top: 150px; font-size: 28px; }
  .origins { position: absolute; left: 40px; top: 200px; width: 200px; font-family: "Playfair Display", serif; font-style: italic; font-size: 14px; line-height: 1.35; text-align: center; color: #e9c48f; }

  /* page 4 */
  .page--specialty .photo { right: 0; bottom: 0; width: 300px; height: 170px; background: radial-gradient(ellipse at 50% 55%, #d5a565 0%, #9c6a34 35%, #3a2614 70%, #111 100%); }
  .page--specialty .brand { right: 34px; top: 34px; font-size: 30px; }
  .spec-block { position: absolute; width: 240px; }
  .spec-block--specialty { left: 22px; top: 28px; }
  .spec-block--taste { left: 22px; top: 160px; }
  .spec-block--note { left: 22px; top: 262px; }
  .spec-block--usp { left: 300px; top: 120px; width: 240px; }
  .contact-box { position: absolute; right: 18px; bottom: 20px; width: 96px; height: 60px; border: 1.5px solid var(--line); border-radius: 8px; background: #000; display: flex; align-items: center; justify-content: center; font-family: "Playfair Display", serif; font-style: italic; font-weight: 600; font-size: 17px; }
</style>
</head>
<body>

<section class="page page--about">
  <div class="photo" role="img" aria-label="Photo of a latte with latte art being poured"></div>
  <div class="brand"><span>Vireo</span><span class="brand__dot"></span></div>
  <div class="info-box info-box--about">
    <h2 class="heading">About Us</h2>
    <p class="body-text">Four friends with one passion for specialty coffee, served with care.</p>
  </div>
  <div class="info-box info-box--market">
    <h2 class="heading">Target Market</h2>
    <p class="body-text">Coffee lovers who value quality, origin and craft in every cup.</p>
  </div>
  <aside class="menu">
    <h2 class="menu__title">Draft Menu</h2>
    <h3 class="menu__group">Coffee</h3>
    <ul class="menu__list">
      <li>Espresso</li><li>Latte</li><li>Cappuccino</li><li>Flat White</li><li>Mocha</li><li>Q45</li><li>Slow Brew</li>
    </ul>
    <div class="menu__rule"></div>
    <h3 class="menu__group">Sweet</h3>
    <ul class="menu__list">
      <li>Waffle</li><li>Cookies</li><li>Cake</li><li>Brownie</li>
    </ul>
  </aside>
</section>

<section class="page page--concept">
  <div class="photo" role="img" aria-label="Photo of an iced coffee in a mason jar with coffee beans"></div>
  <div class="brand"><span>Vireo</span><span class="brand__dot"></span></div>
  <div class="concept-block concept-block--design">
    <h2 class="heading">Design Concept</h2>
    <p class="body-text">Dark tones and warm light frame every cup, letting coffee take center stage.</p>
  </div>
  <div class="concept-block concept-block--investors">
    <h2 class="heading">Investors</h2>
    <p class="body-text">Four friends since college, united by a passion for great coffee and trusted quality.</p>
  </div>
  <div class="investor-row">
    <div class="investor-card">Tarek Bensouda</div>
    <div class="investor-card">Yousef Qandil</div>
    <div class="investor-card">Omar Zaytouni</div>
  </div>
</section>

<section class="page page--vision">
  <div class="photo" role="img" aria-label="Photo of a pour-over coffee dripper on a glass server"></div>
  <div class="statement statement--vision">
    <h2 class="statement__title">Vision</h2>
    <p class="statement__text">Our vision is to be the world benchmark for quality coffee.</p>
  </div>
  <div class="brand"><span>Vireo</span><span class="brand__dot"></span></div>
  <p class="origins">Coffee is come from Colombia, Ethiopia, Kenya, Panama</p>
  <div class="statement statement--mission">
    <h2 class="statement__title">Mission</h2>
    <p class="statement__text">Our mission is to gather people together over a cup of coffee.</p>
  </div>
</section>

<section class="page page--specialty">
  <div class="photo" role="img" aria-label="Photo of waffles with syrup"></div>
  <div class="spec-block spec-block--specialty">
    <h2 class="heading">Specialty Coffee</h2>
    <p class="body-text">Coffee scoring 80 points or above on the PBGN scale is graded specialty.</p>
  </div>
  <div class="brand"><span>Vireo</span><span class="brand__dot"></span></div>
  <div class="spec-block spec-block--taste">
    <h2 class="heading">Taste</h2>
    <p class="body-text">Every bean tastes different, from nutty notes to floral finishes, strong or sweet.</p>
  </div>
  <div class="spec-block spec-block--note">
    <h2 class="heading">Note</h2>
    <p class="body-text">We select only from certified specialty coffee suppliers worldwide.</p>
  </div>
  <div class="spec-block spec-block--usp">
    <h2 class="heading">Unique Selling Propositions</h2>
    <p class="body-text">Only the world's finest specialty coffee, served by certified baristas from bean to cup.</p>
  </div>
  <div class="contact-box">Contact</div>
</section>

</body>
</html>
```